Gourmet food company looking for a dazzling label for their premuim vinagrette dressings

Need a food label that will dazzle our customer and prove what a premium product we have. We make high end gourmet dressing for vegetables, fruit, meat, poultry and fish.

Our label will fit on a 250 mil Tolvenna Square bottle. Labels should be a 4x5 or even 5x5 depending on the design. Nutritionals, bar codes and company blurb will be supplied later. We really want to test you all's talent on this one and are very excited to see your renderings!

Our dressings are Champagne Pear Vinaigrette, White Balsmic Vinaigrette, Mojito Lime Vinaigrette, Creamy-Avacado Lime Vinaigrette, and Asian Sesame Vinaigrette. I hope these names will help you envision our product and kinda what we are looking for.

Thank you all so far for your renderings.I really don't want pictures if that helps. Our logo can be smaller and/or the name of the product bigger. Perhaps we can even redesign Lumora and remove the leaf as I don't really care for what I see yet.So good luck and thanks Added Friday, August 19, 2016

I am still looking for that clean - elegant design for our product as our product is just that. If you look on the internet at vinegars and oils you will see many designs that are simple yet elegant. Creative lettering, bordering, color (can be black and white) and size will help accomplish this. So I invite you to use all your creativity and help me find just what we need.Many thanks Added Tuesday, August 23, 2016

Project Deadline Extended Reason: So many great designs coming in that I wanted a few extra days to tweek!Great job all Added Friday, August 26, 2016

Project Deadline Extended Reason: Very good designs thus far. We just need a few more days.Thanks Added Wednesday, August 31, 2016

Target Market(s)

High end grocery and specialty stores.

Our side panel on the label will say "At Lumora we're fanatics for great flavors and are passionate about finding the best ingredients. From simple to elegant our products are "simply lumora".

Industry/Entity Type

It Company

Font styles to use
Serif
Decorative
Script

Requirements
Must have
• A label that will draw the consumer to pick it up! Need something bold and elegant...
Nice to have
• Again, I really would like to have a label that pops. Since the bottle front is only about 2inches in width it will need some creativity. Would like something very simple and elegant.
• If the designer does not like the logo, please feel free to design without it!
Should not have
• Dark dark colors. We are selling dressing and we don't want any colors that may distort the contents.
• No stock photos for the front. I don't want our dressing to look like the others on the self. Brackwell Pantry just uses lettering and a their packaging is eye catching

```html
<!DOCTYPE html>
<html lang="en">
<head>
<meta charset="utf-8">
<title>Lumora Champagne Pear Vinaigrette Label</title>
<link rel="stylesheet" href="https://fonts.googleapis.com/css2?family=Pinyon+Script&family=Playfair+Display:ital,wght@0,700;1,400&family=Cormorant+Garamond:wght@500&display=swap">
<style>
  :root {
    --backdrop: #eeeeee;
    --label-white: #ffffff;
    --panel-cream: #f3f0ed;
    --olive: #8e9a6a;
    --bark: #5b4b1f;
    --ink: #2b2622;
    --rule-grey: #a9a19a;
    --ornament-haze: #e9e4de;
  }
  * { margin: 0; padding: 0; box-sizing: border-box; }
  html, body {
    width: 781px;
    height: 1200px;
    overflow: hidden;
    background: var(--backdrop);
  }
  .canvas {
    position: relative;
    width: 781px;
    height: 1200px;
  }
  .label {
    position: absolute;
    left: 89px;
    top: 295px;
    width: 611px;
    height: 608px;
    background: var(--label-white);
    box-shadow: 0 8px 22px rgba(0, 0, 0, 0.35);
  }
  .front-panel {
    position: absolute;
    left: 13px;
    top: 14px;
    width: 583px;
    height: 441px;
    background: var(--panel-cream);
  }
  .corner-frame {
    position: absolute;
    width: 64px;
    height: 64px;
  }
  .corner-frame--tl { left: 6px; top: 4px; }
  .corner-frame--tr { right: 6px; top: 4px; transform: scaleX(-1); }
  .corner-frame--bl { left: 6px; bottom: 4px; transform: scaleY(-1); }
  .corner-frame--br { right: 6px; bottom: 4px; transform: scale(-1, -1); }
  .brand-name {
    position: absolute;
    left: 0;
    right: 0;
    top: 80px;
    text-align: center;
    font-family: "Cormorant Garamond", serif;
    font-weight: 500;
    font-size: 19px;
    letter-spacing: 6px;
    color: var(--ink);
    text-transform: uppercase;
  }
  .gate-ornament {
    position: absolute;
    left: 140px;
    top: 160px;
    width: 304px;
    height: 46px;
    background: var(--ornament-haze);
    border-radius: 3px;
  }
  .product-flavour {
    position: absolute;
    left: 0;
    right: 0;
    top: 160px;
    text-align: center;
    font-family: "Pinyon Script", cursive;
    font-size: 66px;
    line-height: 1;
    color: var(--olive);
  }
  .product-type {
    position: absolute;
    left: 0;
    right: 0;
    top: 242px;
    text-align: center;
    font-family: "Playfair Display", serif;
    font-weight: 700;
    font-size: 43px;
    line-height: 1;
    letter-spacing: 1px;
    color: var(--bark);
  }
  .dotted-rule {
    position: absolute;
    left: 201px;
    top: 296px;
    width: 182px;
    border-top: 2px dotted var(--rule-grey);
  }
  .volume {
    position: absolute;
    left: 0;
    right: 0;
    top: 512px;
    text-align: center;
    font-family: "Playfair Display", serif;
    color: var(--olive);
    font-size: 27px;
  }
  .volume__number { font-weight: 700; }
  .volume__unit { font-style: italic; font-weight: 400; font-size: 22px; }
</style>
</head>
<body>
<main class="canvas">
  <article class="label">
    <section class="front-panel">
      <svg class="corner-frame corner-frame--tl" viewBox="0 0 64 64" aria-hidden="true">
        <g fill="none" stroke="var(--rule-grey)" stroke-width="1.2">
          <path d="M2 2 H62 M2 2 V62"/>
          <path d="M6 6 H58 M6 6 V58"/>
          <path d="M10 10 H40 M10 10 V40"/>
        </g>
      </svg>
      <svg class="corner-frame corner-frame--tr" viewBox="0 0 64 64" aria-hidden="true">
        <g fill="none" stroke="var(--rule-grey)" stroke-width="1.2">
          <path d="M2 2 H62 M2 2 V62"/>
          <path d="M6 6 H58 M6 6 V58"/>
          <path d="M10 10 H40 M10 10 V40"/>
        </g>
      </svg>
      <svg class="corner-frame corner-frame--bl" viewBox="0 0 64 64" aria-hidden="true">
        <g fill="none" stroke="var(--rule-grey)" stroke-width="1.2">
          <path d="M2 2 H62 M2 2 V62"/>
          <path d="M6 6 H58 M6 6 V58"/>
          <path d="M10 10 H40 M10 10 V40"/>
        </g>
      </svg>
      <svg class="corner-frame corner-frame--br" viewBox="0 0 64 64" aria-hidden="true">
        <g fill="none" stroke="var(--rule-grey)" stroke-width="1.2">
          <path d="M2 2 H62 M2 2 V62"/>
          <path d="M6 6 H58 M6 6 V58"/>
          <path d="M10 10 H40 M10 10 V40"/>
        </g>
      </svg>

      <p class="brand-name">Lumora</p>

      <div class="gate-ornament" role="img" aria-label="Faint ornamental wrought-iron gate motif behind the product name"></div>

      <h1 class="product-flavour">Champagne Pear</h1>
      <h2 class="product-type">VINAIGRETTE</h2>
      <div class="dotted-rule"></div>
    </section>

    <p class="volume"><span class="volume__number">250</span> <span class="volume__unit">mil</span></p>
  </article>
</main>
</body>
</html>
```